Real Estate Development Company Stationary

We need our company, business card, letterhead, pocket folder and envelope designed.

We are a new real estate development company. We focus on data centre, commercial and real estate development.

Please see attached for our logo. Since it's a new logo, you still can make minor adjust if you like it makes senses

The client has sent me a business card he really likes. Please see file 3.

Target Market(s)

Real Estate Investors
Large corporations
Home buyers

Industry/Entity Type

Real Estate

```html
<!DOCTYPE html>
<html lang="en">
<head>
<meta charset="utf-8">
<title>Vantor Development Inc. – Pocket Folder</title>
<link rel="stylesheet" href="https://fonts.googleapis.com/css2?family=Questrial&display=swap">
<style>
  :root {
    --backdrop: #f4f4f4;
    --folder: #fbfbfb;
    --folder-edge: #e2e2e2;
    --pocket: #f7f7f7;
    --sheet: #ffffff;
    --brand-green: #6cb33f;
    --rule-blue: #2f4f96;
    --ink: #3a3a3a;
  }
  * { box-sizing: border-box; margin: 0; padding: 0; }
  html, body { width: 1200px; height: 800px; overflow: hidden; }
  body {
    background: var(--backdrop);
    font-family: "Questrial", sans-serif;
    color: var(--ink);
  }
  .folder {
    position: absolute;
    left: 110px; top: 70px;
    width: 980px; height: 660px;
    display: flex;
    box-shadow: 0 10px 30px rgba(0,0,0,.12);
  }
  .panel {
    position: relative;
    width: 490px; height: 660px;
    background: var(--folder);
    overflow: hidden;
  }
  .panel--left { border-right: 1px solid var(--folder-edge); }
  .sheet {
    position: absolute;
    left: 30px; top: 28px;
    width: 430px; height: 560px;
    background: var(--sheet);
    box-shadow: 0 1px 4px rgba(0,0,0,.12);
    padding: 26px 30px;
    overflow: hidden;
  }
  .letterhead-top {
    display: flex;
    align-items: center;
    gap: 8px;
    border-bottom: 1.5px solid var(--rule-blue);
    padding-bottom: 10px;
  }
  .brand-mark {
    width: 12px; height: 12px;
    border-radius: 50%;
    background: var(--brand-green);
  }
  .brand-name {
    color: var(--brand-green);
    font-size: 15px;
    letter-spacing: .5px;
  }
  .letter-body { font-size: 8.5px; line-height: 1.55; margin-top: 22px; }
  .letter-date { margin-bottom: 18px; }
  .letter-salutation { margin-bottom: 20px; }
  .letter-body p { margin-bottom: 14px; }
  .pocket {
    position: absolute;
    left: 0; right: 0; bottom: 0;
    background: var(--pocket);
    border-top: 1px solid var(--folder-edge);
    box-shadow: 0 -2px 6px rgba(0,0,0,.06);
  }
  .panel--left .pocket { top: 300px; }
  .panel--right .pocket { top: 200px; }
  .pocket-brand {
    position: absolute;
    right: 40px; top: 70px;
    display: flex;
    align-items: center;
    gap: 12px;
  }
  .pocket-brand .brand-mark { width: 26px; height: 26px; }
  .pocket-brand .brand-name { font-size: 26px; }
</style>
</head>
<body>
  <main class="folder">
    <section class="panel panel--left">
      <article class="sheet">
        <header class="letterhead-top">
          <span class="brand-mark"></span>
          <span class="brand-name">Vantor Development Inc.</span>
        </header>
        <div class="letter-body">
          <p class="letter-date">January 12, 2015</p>
          <p class="letter-salutation">Massa amet luctus<br>lorem ipsum dolor sit amet,<br>eros pellentesque.</p>
          <p>Lorem ipsum dolor sit amet, eros pellentesque, eget iaculis pulvinar, erat sed elit luctus venenatis leo. Wisi sit nunc morbi ab in nunc accumsan urna. Ipsum consectetuer, eleifend eros mauris. Consectetuer provident magna cras vestibulum posuere nonummy, suspendisse aenean mus dolor cras cursus. Nec congue, vivamus accumsan, cumque ipsum venenatis justo a congue vel vestibulum cras primis id, sed ante.</p>
          <p>Tellus hendrerit scelerisque sapien mus ut vestibulum, neque sapien semper mauris, est aliquam fusce tortor amet ornare sapien dictumst. Risus amet eu dui pellentesque, porttitor nec sagittis vitae lacinia donec vitae libero in cursus blandit morbi lacinia justo pede nunc orci ullamcorper.</p>
        </div>
      </article>
      <div class="pocket"></div>
    </section>

    <section class="panel panel--right">
      <article class="sheet">
        <header class="letterhead-top">
          <span class="brand-mark"></span>
          <span class="brand-name">Vantor Development Inc.</span>
        </header>
        <div class="letter-body">
          <p class="letter-date">January 12, 2015</p>
          <p class="letter-salutation">Massa amet luctus<br>lorem ipsum dolor sit amet,<br>eros pellentesque.</p>
          <p>Lorem ipsum dolor sit amet, eros pellentesque, eget iaculis pulvinar, erat sed elit luctus venenatis leo. Wisi sit nunc morbi ab in nunc accumsan urna. Ipsum consectetuer, eleifend eros mauris. Consectetuer provident magna cras vestibulum posuere nonummy, suspendisse aenean mus dolor cras cursus. Nec congue, vivamus accumsan, cumque ipsum venenatis justo a congue vel vestibulum cras primis id, sed ante.</p>
          <p>Tellus hendrerit scelerisque sapien mus ut vestibulum, neque sapien semper mauris, est aliquam fusce tortor amet ornare sapien dictumst. Risus amet eu dui pellentesque, porttitor nec sagittis vitae lacinia donec vitae libero in cursus blandit morbi lacinia justo pede nunc orci ullamcorper.</p>
        </div>
      </article>
      <div class="pocket">
        <div class="pocket-brand">
          <span class="brand-mark"></span>
          <span class="brand-name">Vantor Development Inc.</span>
        </div>
      </div>
    </section>
  </main>
</body>
</html>
```